Business Card

Just need business logo with phone number on it. 0487 312 556
And the following on the bottom of the card.

"Your local plumbing experts".
and emblems for kelpa card, cheque and cash

```html
<!DOCTYPE html>
<html lang="en">
<head>
<meta charset="utf-8">
<title>Harbourside Plumbing &amp; Drainage – Business Card</title>
<link href="https://fonts.googleapis.com/css2?family=Roboto:wght@400;700;900&display=swap" rel="stylesheet">
<style>
  :root{
    --bg:#e9e7e3;
    --card:#ffffff;
    --red:#dc1f2e;
    --blue:#1ea7d6;
    --blue-deep:#1b8fc4;
    --slate:#5d6675;
    --cash-dark:#4c5a52;
    --cash-green:#6dbb4a;
    --card-gold:#e8a91d;
    --card-navy:#1f3a8a;
  }
  *{margin:0;padding:0;box-sizing:border-box}
  html,body{width:1200px;height:780px;overflow:hidden;background:var(--bg)}
  body{font-family:"Roboto",Arial,sans-serif;position:relative}
  .business-card{
    position:absolute;left:100px;top:104px;width:1000px;height:572px;
    background:var(--card);overflow:hidden;
    box-shadow:0 10px 30px rgba(0,0,0,.18);
  }
  .card-bands{position:absolute;inset:0}
  .brand{
    position:absolute;left:360px;top:120px;width:520px;
    display:flex;align-items:center;gap:18px;
  }
  .brand-mark{width:22px;height:22px;border-radius:50%;background:var(--red);flex:none}
  .brand-name{
    font-weight:900;color:var(--red);text-transform:uppercase;
    font-size:46px;line-height:1;letter-spacing:1px;
  }
  .brand-sub{
    display:block;font-size:24px;letter-spacing:7px;margin-top:10px;
  }
  .brand-legal{
    display:block;font-size:11px;letter-spacing:3px;margin-top:8px;
  }
  .phone{
    position:absolute;left:250px;top:300px;font-size:42px;font-weight:400;
    color:var(--blue);letter-spacing:1px;
  }
  .phone .label{color:var(--red)}
  .payment-methods{
    position:absolute;left:255px;top:375px;display:flex;align-items:center;gap:36px;
  }
  .method-kelpa{
    width:120px;height:66px;border:2px solid var(--slate);border-radius:6px;
    display:flex;align-items:center;justify-content:center;gap:8px;
    font-weight:700;font-size:24px;color:var(--card-navy);letter-spacing:1px;
  }
  .method-kelpa .chip{width:12px;height:12px;background:var(--card-gold)}
  .tagline{
    position:absolute;left:250px;top:488px;font-size:36px;font-weight:400;
    color:var(--blue);letter-spacing:1.5px;
  }
</style>
</head>
<body>
  <main class="business-card">
    <svg class="card-bands" viewBox="0 0 1000 572" width="1000" height="572" aria-hidden="true">
      <path fill="var(--red)" d="M0,0 H300 Q110,286 230,572 H0 Z"/>
      <path fill="var(--blue)" d="M790,0 Q960,330 680,572 H1000 V0 Z"/>
      <path fill="var(--blue-deep)" opacity=".35" d="M900,0 Q1000,300 860,572 H1000 V0 Z"/>
    </svg>

    <div class="brand">
      <span class="brand-mark" aria-hidden="true"></span>
      <p class="brand-name">Harbourside
        <span class="brand-sub">Plumbing &amp; Drainage</span>
        <span class="brand-legal">Pty Ltd</span>
      </p>
    </div>

    <p class="phone"><span class="label">P:</span> 0487 312 556</p>

    <div class="payment-methods">
      <div class="method-kelpa"><span class="chip" aria-hidden="true"></span>KELPA</div>
      <svg class="method-cash" width="72" height="72" viewBox="0 0 72 72" role="img" aria-label="Cash">
        <circle cx="36" cy="36" r="34" fill="var(--cash-dark)"/>
        <rect x="14" y="24" width="40" height="22" rx="2" fill="var(--cash-green)" transform="rotate(-10 34 35)"/>
        <rect x="20" y="30" width="40" height="22" rx="2" fill="#8fd16a" transform="rotate(-10 40 41)"/>
        <circle cx="40" cy="41" r="5" fill="var(--cash-dark)" opacity=".5"/>
      </svg>
      <svg class="method-cheque" width="96" height="72" viewBox="0 0 96 72" role="img" aria-label="Cheque">
        <rect x="4" y="16" width="84" height="50" rx="5" fill="none" stroke="var(--slate)" stroke-width="5"/>
        <text x="20" y="54" font-family="Roboto, Arial, sans-serif" font-weight="700" font-size="22" fill="var(--slate)">$</text>
        <line x1="42" y1="40" x2="76" y2="40" stroke="var(--slate)" stroke-width="4"/>
        <line x1="42" y1="52" x2="70" y2="52" stroke="var(--slate)" stroke-width="4"/>
        <line x1="40" y1="30" x2="70" y2="4" stroke="var(--blue)" stroke-width="6" stroke-linecap="round"/>
      </svg>
    </div>

    <p class="tagline">Your local plumbing experts</p>
  </main>
</body>
</html>
```